Brightmere Business Card Redesign & Logo Update

We need to update our business cards to something more modern and fresh. Brightmere can provide the current color schemes and old design examples, but welcome creativity in helping us with this redesign. PLEASE NOTE that we no longer utilize the "tree" and/or "leaf" imagery in our branding. If able would apprecaite an update on the quality of our "words only" logo in Ai. / PNG formats too.

Target Market(s)

Investors, landowners, corporate partners, contractors

Industry/Entity Type

Environmental Restoration & Conservation

Contact Information for Business Card

Logo, persons name, title, mailing address, phone and email, website url

Font styles to use
Other font styles liked:
• Merriweather

Requirements
Nice to have
• Logo, persons name, title, mailing address, phone and email, website url, but open to ideams
Should not have
• No all back backgrounds

```html
<!DOCTYPE html>
<html lang="en">
<head>
<meta charset="utf-8">
<title>Brightmere Business Card</title>
<link rel="stylesheet" href="https://fonts.googleapis.com/css2?family=Open+Sans:wght@400;700&display=swap">
<style>
  :root {
    --backdrop: #dcdcda;
    --paper: #ffffff;
    --brand-green: #1a7c3e;
    --brand-orange: #ee7c22;
    --ink-grey: #6b6b6b;
    --rule-green: #8fbf9f;
  }
  * { box-sizing: border-box; margin: 0; padding: 0; }
  html, body {
    width: 1200px; height: 801px; overflow: hidden;
    background: var(--backdrop);
    font-family: "Open Sans", Arial, sans-serif;
  }
  .sheet {
    position: relative; width: 1200px; height: 801px;
  }
  .card {
    position: absolute; top: 252px;
    width: 520px; height: 297px;
    background: var(--paper);
    border-bottom: 3px solid var(--brand-green);
    box-shadow: 0 2px 6px rgba(0,0,0,0.12);
    overflow: hidden;
  }
  .card--front { left: 50px; }
  .card--back { left: 630px; }

  .wordmark {
    font-weight: 700; color: var(--brand-green);
    text-transform: uppercase; letter-spacing: 1px; line-height: 1;
  }
  .card--front .wordmark {
    position: absolute; left: 60px; top: 52px; font-size: 44px;
  }
  .card--back .wordmark {
    position: absolute; left: 0; right: 0; top: 118px;
    text-align: center; font-size: 58px;
  }

  .person {
    position: absolute; right: 292px; top: 140px; text-align: right;
  }
  .person__name {
    font-weight: 700; font-size: 17px; color: var(--brand-green);
    text-transform: uppercase; letter-spacing: 0.5px;
  }
  .person__title { font-size: 14px; color: var(--ink-grey); }

  .divider {
    position: absolute; left: 245px; top: 128px;
    width: 1px; height: 66px; background: var(--rule-green);
  }

  .contacts {
    position: absolute; left: 262px; top: 124px; list-style: none;
  }
  .contacts li {
    display: flex; align-items: center; gap: 7px;
    font-size: 13px; color: var(--ink-grey); line-height: 23px;
  }
  .contacts svg { width: 11px; height: 11px; flex: none; }

  .address-band {
    position: absolute; left: 0; right: 0; top: 226px; height: 36px;
    background: var(--brand-green); color: var(--paper);
    font-size: 14px; display: flex; align-items: center; justify-content: center;
    letter-spacing: 0.3px;
  }
</style>
</head>
<body>
<main class="sheet">
  <section class="card card--front" aria-label="Card front">
    <div class="wordmark">Brightmere</div>

    <div class="person">
      <div class="person__name">Dorian Halvey</div>
      <div class="person__title">President</div>
    </div>

    <div class="divider"></div>

    <ul class="contacts">
      <li>
        <svg viewBox="0 0 12 12" aria-hidden="true"><path fill="var(--brand-orange)" d="M2.5 1h2l1 2.6-1.3.9a6 6 0 0 0 3.3 3.3l.9-1.3 2.6 1v2A1.5 1.5 0 0 1 9.5 11 8.5 8.5 0 0 1 1 2.5 1.5 1.5 0 0 1 2.5 1z"/></svg>
        555-310-4872
      </li>
      <li>
        <svg viewBox="0 0 12 12" aria-hidden="true"><rect x="0.5" y="2" width="11" height="8" fill="var(--brand-orange)"/><path d="M0.8 2.4 6 6.5l5.2-4.1" fill="none" stroke="#fff" stroke-width="1"/></svg>
        dhalvey@brightmere.com
      </li>
      <li>
        <svg viewBox="0 0 12 12" aria-hidden="true"><circle cx="6" cy="6" r="5.5" fill="var(--brand-orange)"/><path d="M0.5 6h11M6 .5c-3 3-3 8 0 11M6 .5c3 3 3 8 0 11" fill="none" stroke="#fff" stroke-width="0.8"/></svg>
        www.brightmere.com
      </li>
    </ul>

    <div class="address-band">18420 Harbor Crest Dr, Seaview CA 92601</div>
  </section>

  <section class="card card--back" aria-label="Card back">
    <div class="wordmark">Brightmere</div>
  </section>
</main>
</body>
</html>
```